Side of Page Partnership-type Letterhead Design for Chiropractic Office

Side oriented letterhead with practice locations/demographics, physician names and company logo

Target Market(s)

Healthcare Professionals & Attorneys

Industry/Entity Type

Healthcare

Font styles to use
Other font styles liked:
• Font of Logo is Trajan Pro, but not a deal breaker if we try something else

Colors

Designer to choose colors to be used in the design.

Requirements
Must have
• All info from attached documents

```html
<!DOCTYPE html>
<html lang="en">
<head>
<meta charset="utf-8">
<title>Keystone Chiropractic Letterhead</title>
<link href="https://fonts.googleapis.com/css2?family=Arimo:wght@400;700&family=Roboto+Condensed:wght@400;700&display=swap" rel="stylesheet">
<style>
  :root {
    --bg: #e3e3e3;
    --paper: #ffffff;
    --blue: #2e3a8f;
    --orange: #f29111;
    --green: #6aa43a;
    --ink: #222222;
    --grey: #8a8a8a;
    --rule: #e2e2e2;
    --text: #333333;
  }
  * { box-sizing: border-box; margin: 0; padding: 0; }
  html, body { width: 1200px; height: 784px; overflow: hidden; background: var(--bg); }
  .letterhead {
    position: absolute; left: 377px; top: 32px;
    width: 446px; height: 720px;
    background: var(--paper);
    box-shadow: 0 2px 8px rgba(0,0,0,.12);
    font-family: "Arimo", Arial, sans-serif;
    color: var(--text);
  }
  .top-bar { position: absolute; left: 0; top: 26px; width: 44px; height: 5px; background: var(--blue); }
  .brand {
    position: absolute; left: 52px; top: 14px;
    font-family: "Arimo", Arial, sans-serif; font-weight: 400;
    font-size: 14px; line-height: 15px; letter-spacing: 2px;
    color: var(--ink); text-transform: uppercase;
  }
  .brand-mark { position: absolute; left: 178px; top: 20px; width: 16px; height: 16px; border-radius: 50%; background: var(--green); }
  .top-rule { position: absolute; left: 204px; right: 0; top: 40px; height: 3px; background: var(--orange); }

  .sidebar { position: absolute; left: 26px; top: 150px; width: 74px; }
  .doctors { list-style: none; margin-bottom: 18px; }
  .doctors li {
    position: relative; padding-left: 8px;
    font-family: "Roboto Condensed", Arial, sans-serif; font-weight: 700;
    font-size: 6.2px; line-height: 10px; color: var(--blue);
  }
  .doctors li::before {
    content: ""; position: absolute; left: 0; top: 2.5px;
    border-left: 5px solid var(--orange); border-top: 2.5px solid transparent; border-bottom: 2.5px solid transparent;
  }
  .office { margin-bottom: 18px; font-family: "Roboto Condensed", Arial, sans-serif; font-size: 5.8px; line-height: 8.5px; color: var(--grey); }
  .office-name { position: relative; padding-left: 8px; font-weight: 700; font-size: 6.4px; color: var(--blue); }
  .office-name::before { content: ""; position: absolute; left: 0; top: 2px; width: 5px; height: 5px; border-radius: 50%; background: var(--blue); }
  .office p { padding-left: 8px; }
  .office .label { font-weight: 700; color: var(--blue); }

  .divider { position: absolute; left: 106px; top: 132px; width: 1px; height: 420px; background: var(--rule); }

  .letter-body { position: absolute; left: 120px; top: 152px; width: 300px; font-size: 6.8px; line-height: 9.6px; }
  .letter-body p { margin-bottom: 9.6px; }

  .signature {
    position: absolute; left: 250px; top: 520px; width: 110px; height: 34px;
    background: linear-gradient(90deg, #f1f1f1, #e8e8e8);
  }

  .edge-green { position: absolute; left: 0; width: 98px; bottom: 14px; height: 3px; background: var(--green); }
  .edge-blue { position: absolute; left: 100px; width: 100px; bottom: 14px; height: 3px; background: var(--blue); }
  .edge-orange { position: absolute; left: 202px; width: 112px; bottom: 14px; height: 3px; background: var(--orange); }
  .edge-base { position: absolute; left: 0; right: 0; bottom: 0; height: 5px; background: var(--ink); }
  .web-band {
    position: absolute; left: 316px; right: 0; bottom: 0; height: 20px;
    background: var(--ink); color: #fff;
    font-family: "Arimo", Arial, sans-serif; font-weight: 700;
    font-size: 7.5px; line-height: 20px; text-align: center; letter-spacing: .2px;
  }
</style>
</head>
<body>
  <main class="letterhead">
    <div class="top-bar"></div>
    <div class="brand">Keystone<br>Chiropractic</div>
    <div class="brand-mark"></div>
    <div class="top-rule"></div>

    <aside class="sidebar">
      <ul class="doctors">
        <li>Daniel Ortego, DC, DACNB</li>
        <li>Neil Ortego, DC</li>
        <li>Grant Wexley, DC</li>
        <li>Owen Pryce, DC</li>
        <li>Luke Danvers, DC</li>
        <li>Evan Castell, DC</li>
        <li>Miles Carver, DC</li>
      </ul>
      <div class="office">
        <div class="office-name">Northvale</div>
        <p>4120 N. Market St.</p>
        <p>Northvale, OH 43001</p>
        <p><span class="label">P:</span> 555-0142</p>
        <p><span class="label">F:</span> 555-0143</p>
      </div>
      <div class="office">
        <div class="office-name">Westhaven</div>
        <p>218 S. Grove St.</p>
        <p>Westhaven, OH 43002</p>
        <p><span class="label">P:</span> 555-0168</p>
        <p><span class="label">F:</span> 555-0169</p>
      </div>
      <div class="office">
        <div class="office-name">Eastmoor</div>
        <p>905 E. Linden Rd</p>
        <p>Eastmoor, OH 43003</p>
        <p><span class="label">P:</span> 555-0187</p>
        <p><span class="label">F:</span> 555-0188</p>
      </div>
    </aside>

    <div class="divider"></div>

    <section class="letter-body">
      <p>Lorem ipsum is simply dummy text of the printing and typesetting industry. Lorem ipsum has been the industry's standard dummy text ever since the 1500s, when an unknown printer took a galley of type and scrambled it to make a type specimen book. It has survived not only five centuries, but also the leap into electronic typesetting, remaining essentially unchanged. It was popularised in the 1960s with the release of sheets containing Lorem ipsum passages, and more recently with desktop publishing software including versions of Lorem ipsum.</p>
      <p>It is a long established fact that a reader will be distracted by the readable content of a page when looking at its layout. The point of using Lorem ipsum is that it has a more-or-less normal distribution of letters, as opposed to using 'Content here, content here', making it look like readable English. Many desktop publishing packages and web page editors now use Lorem ipsum as their default model text, and a search for 'lorem ipsum' will uncover many web sites still in their infancy. Various versions have evolved over the years, sometimes by accident, sometimes on purpose (injected humour and the like).</p>
      <p>Contrary to popular belief, Lorem ipsum is not simply random text. It has roots in a piece of classical Latin literature from 45 BC, making it over 2000 years old. A Latin scholar looked up one of the more obscure Latin words, consectetur, from a Lorem ipsum passage, and going through the cites of the word in classical literature, discovered the undoubtable source. Lorem ipsum comes from sections 1.10.32 and 1.10.33 of "de Finibus Bonorum et Malorum". The generated Lorem ipsum is therefore always free from repetition, injected humour, or non-characteristic words etc.</p>
    </section>

    <div class="signature" role="img" aria-label="Handwritten signature of the sender"></div>

    <div class="edge-green"></div>
    <div class="edge-blue"></div>
    <div class="edge-orange"></div>
    <div class="edge-base"></div>
    <div class="web-band">www.keystonechiropractic.com</div>
  </main>
</body>
</html>
```